public page kestrel AX (www.kestrelax.com)

https://www.plumaquill.com/shard/s418/sh/b2190ce7-5d3a-4f1e-8c2b-6e7a1d94c0f2/47b1e9c2d0a83f56e1c7b9a2f4d60e81

compatible with wordpress

Designs look the same

Industry/Entity Type

Finance And Accounting

Coding

Coded - Design and coding required

Number of Pages Required

1 page

Font styles to use
Sans Serif

Colors
85cae6
3176b5
cfdeed
fac994
fff3d1
fefdec
cfcfcf
e8e8e8
9d9d9d

```html
<!DOCTYPE html>
<html lang="en">
<head>
<meta charset="utf-8">
<title>kestrel AX – Calculate your numbers</title>
<link rel="stylesheet" href="https://fonts.googleapis.com/css2?family=Montserrat:wght@300;400;500;600;700&display=swap">
<style>
:root{
  --grad-start:#3a28e6;
  --grad-end:#2ba7c6;
  --accent:#fbb52a;
  --accent-dark:#f39c12;
  --ink:#1d1d2b;
  --muted:#7a7f8a;
  --soft-bg:#f2f8fc;
  --line:#cfcfcf;
  --card-line:#e8e8e8;
  --white:#ffffff;
  --navy:#13294a;
}
*{box-sizing:border-box;margin:0;padding:0}
html,body{width:1200px;height:3125px;overflow:hidden}
body{font-family:"Montserrat",Arial,sans-serif;color:var(--ink);background:var(--white);position:relative}
section,header,footer{position:absolute;left:0;width:1200px}
.abs{position:absolute}
.gradient{background:linear-gradient(100deg,var(--grad-start) 0%,#3560dc 45%,var(--grad-end) 100%)}
.btn{position:absolute;display:flex;align-items:center;justify-content:center;background:var(--accent);color:var(--white);font-weight:600;font-size:13px;border-radius:20px;box-shadow:0 4px 10px rgba(243,156,18,.35)}
/* header / hero */
.hero{top:0;height:490px;color:var(--white);overflow:hidden}
.hero::after{content:"";position:absolute;left:-100px;top:-200px;width:700px;height:900px;background:rgba(255,255,255,.05);transform:rotate(25deg)}
.brand{position:absolute;display:flex;align-items:center;gap:10px;font-size:17px;font-weight:400;color:var(--white)}
.brand-dot{width:34px;height:34px;border-radius:50%;background:var(--white);opacity:.95}
.nav{position:absolute;top:32px;font-size:12px;font-weight:500}
.nav a{position:absolute;color:var(--white);text-decoration:none;white-space:nowrap}
.btn-login{position:absolute;left:904px;top:27px;width:67px;height:29px;border:1.5px solid var(--white);border-radius:5px;font-size:12px;display:flex;align-items:center;justify-content:center}
.btn-signup{position:absolute;left:985px;top:27px;width:63px;height:29px;background:var(--accent);border-radius:5px;font-size:12px;display:flex;align-items:center;justify-content:center}
.hero-title{position:absolute;top:102px;width:100%;text-align:center;font-size:44px;font-weight:400;z-index:1}
.hero-sub{position:absolute;top:163px;width:100%;text-align:center;font-size:22px;letter-spacing:6px;font-weight:400;z-index:1}
.email{position:absolute;left:375px;top:225px;width:325px;height:40px;background:var(--white);border-radius:20px;color:#a6a6a6;font-size:12px;padding-left:24px;display:flex;align-items:center;z-index:1}
.devices-hero{position:absolute;left:202px;top:312px;width:802px;height:261px;border-radius:10px;background:linear-gradient(180deg,#2f3a4d,#e9eef3 30%,#d7dde4);z-index:2;box-shadow:0 12px 30px rgba(0,0,0,.25)}
/* feature sections */
.feature h2{position:absolute;font-size:29px;font-weight:400;line-height:36px;color:var(--ink)}
.feature p{position:absolute;width:400px;font-size:14px;line-height:28px;color:var(--muted)}
.f1{top:490px;height:468px;background:var(--white)}
.f2{top:958px;height:379px;background:var(--soft-bg)}
.f3{top:1337px;height:398px;background:var(--white);overflow:hidden}
.art-phones{left:0;top:72px;width:552px;height:313px;background:linear-gradient(135deg,#e7f6f7,#8ed8d9);border-radius:0 18px 18px 0}
.art-laptops{left:604px;top:100px;width:463px;height:196px;background:linear-gradient(180deg,#2f3a4d,#e9eef3 30%,#d2d9e0);border-radius:8px}
.art-hand{left:156px;top:48px;width:344px;height:350px;background:linear-gradient(160deg,#f1e4da,#b35b3a 55%,#5a2a1c);border-radius:30px 30px 0 0}
/* pricing */
.pricing{top:1735px;height:379px;color:var(--white);text-align:center}
.pricing .mark{position:absolute;left:570px;top:42px;width:60px;height:60px;border-radius:50%;background:var(--white)}
.pricing h2{position:absolute;top:112px;width:100%;font-size:34px;font-weight:400}
.pricing .from{position:absolute;top:170px;width:100%;font-size:19px}
.pricing .price{position:absolute;top:192px;width:100%;font-size:58px;font-weight:400}
/* blog */
.blog{top:2114px;height:452px;background:var(--white)}
.section-title{position:absolute;width:100%;text-align:center;font-size:29px;font-weight:400}
.post{position:absolute;top:111px;width:238px;height:285px;background:var(--white);box-shadow:0 3px 12px rgba(0,0,0,.12);overflow:hidden}
.post-corner{position:absolute;right:0;top:0}
.post-date{position:absolute;left:26px;top:24px;height:22px;padding:0 10px;background:var(--navy);color:var(--white);font-size:10px;font-weight:700;display:flex;align-items:center;border-radius:3px}
.post h3{position:absolute;left:26px;top:60px;font-size:13px;font-weight:700;line-height:17px;color:var(--navy)}
.post p{position:absolute;left:26px;top:102px;width:190px;font-size:12px;line-height:16px;color:var(--ink)}
.post .more{position:absolute;left:26px;top:238px;width:86px;height:22px;background:var(--accent-dark);color:var(--white);font-size:9px;font-weight:700;display:flex;align-items:center;justify-content:center}
/* partners */
.partners{top:2566px;height:300px;background:var(--soft-bg)}
.partner{position:absolute;top:113px;width:203px;height:87px;background:var(--white);border:1px solid var(--card-line);display:flex;align-items:center;justify-content:center}
.partner span{display:block;width:110px;height:22px;border-radius:11px;background:#c4c8cc}
.dots{position:absolute;top:238px;left:555px;display:flex;gap:8px}
.dots i{width:6px;height:6px;border-radius:50%;background:#9d9d9d}
/* footer */
.site-footer{top:2866px;height:259px;color:var(--white);font-size:11px}
.foot-mark{position:absolute;left:192px;top:40px;width:68px;height:68px;border-radius:50%;background:var(--white)}
.contact{position:absolute;left:192px;top:122px;line-height:20px}
.contact div{display:flex;align-items:center;gap:8px}
.foot-col{position:absolute;top:48px}
.foot-col h4{font-size:13px;font-weight:600;margin-bottom:10px}
.foot-col li{list-style:none;line-height:20px}
.foot-rule{position:absolute;left:192px;top:213px;width:816px;height:1px;background:rgba(255,255,255,.35)}
.copyright{position:absolute;left:192px;top:228px;font-size:10px}
.socials{position:absolute;left:941px;top:226px;display:flex;gap:7px}
.socials i{width:18px;height:18px;border-radius:50%;border:1.5px solid var(--white)}
</style>
</head>
<body>

<header class="hero gradient">
  <div class="brand" style="left:146px;top:22px"><span class="brand-dot"></span>kestrel AX</div>
  <nav class="nav">
    <a style="left:433px">Pricing</a>
    <a style="left:505px">About us</a>
    <a style="left:594px">Contact</a>
    <a style="left:679px">Blog</a>
    <a style="left:743px">FAQ's</a>
  </nav>
  <div class="btn-login">Login</div>
  <div class="btn-signup">Sign up</div>
  <h1 class="hero-title">Calculate your numbers</h1>
  <div class="hero-sub">Easier like never before</div>
  <div class="email">Your Email Address</div>
  <div class="btn" style="left:708px;top:225px;width:119px;height:40px;z-index:1">Get started</div>
</header>
<div class="devices-hero" role="img" aria-label="Dashboard screens shown on laptops and monitors"></div>

<section class="feature f1">
  <div class="abs art-phones" role="img" aria-label="Illustration of phones showing the app"></div>
  <h2 style="left:619px;top:162px">We take care of your work<br>just do your job</h2>
  <p style="left:616px;top:248px">A big part of our design process is validation and nailing the details. Lumaframe lets us iterate quickly, elevate quality, and ship fast.</p>
  <div class="btn" style="left:614px;top:372px;width:120px;height:34px">Get started</div>
</section>

<section class="feature f2">
  <h2 style="left:158px;top:60px">Our good feedbacks and<br>statistics shows all</h2>
  <p style="left:156px;top:145px">A big part of our design process is validation and nailing the details. Lumaframe lets us iterate quickly, elevate quality, and ship fast.</p>
  <div class="btn" style="left:156px;top:270px;width:120px;height:34px">Get started</div>
  <div class="abs art-laptops" role="img" aria-label="Laptops showing statistics dashboards"></div>
</section>

<section class="feature f3">
  <div class="abs art-hand" role="img" aria-label="Photo of a hand holding a smartphone"></div>
  <h2 style="left:610px;top:80px">Don't miss your chance<br>to grow</h2>
  <p style="left:608px;top:165px">A big part of our design process is validation and nailing the details. Lumaframe lets us iterate quickly, elevate quality, and ship fast.</p>
  <div class="btn" style="left:603px;top:290px;width:120px;height:34px">Get started</div>
</section>

<section class="pricing gradient">
  <div class="mark"></div>
  <h2>Grab Our Plan Now</h2>
  <div class="from">Only from</div>
  <div class="price">$19,99</div>
  <div class="btn" style="left:506px;top:292px;width:190px;height:46px;font-size:15px;border-radius:23px">Get Started</div>
</section>

<section class="blog">
  <h2 class="section-title" style="top:44px">Our Blog</h2>
  <article class="post" style="left:187px">
    <svg class="post-corner" width="60" height="50" viewBox="0 0 60 50"><path d="M0 0H60V50C60 20 40 4 0 0Z" fill="#13294a"/></svg>
    <div class="post-date">10.01.2017</div>
    <h3>Easy Managed<br>Time Can Save you Money</h3>
    <p>Lorem ipsum dolor sit amet, consectetuer adipiscing elit. Aenean commodo ligula eget dolor. Aenean massa. Cum sociis natoque penatibus et magnis dis parturient montes.</p>
    <div class="more">Read More</div>
  </article>
  <article class="post" style="left:473px">
    <svg class="post-corner" width="60" height="50" viewBox="0 0 60 50"><path d="M0 0H60V50C60 20 40 4 0 0Z" fill="#13294a"/></svg>
    <div class="post-date">10.01.2017</div>
    <h3>Easy Managed<br>Time Can Save you Money</h3>
    <p>Lorem ipsum dolor sit amet, consectetuer adipiscing elit. Aenean commodo ligula eget dolor. Aenean massa. Cum sociis natoque penatibus et magnis dis parturient montes.</p>
    <div class="more">Read More</div>
  </article>
  <article class="post" style="left:758px">
    <svg class="post-corner" width="60" height="50" viewBox="0 0 60 50"><path d="M0 0H60V50C60 20 40 4 0 0Z" fill="#13294a"/></svg>
    <div class="post-date">10.01.2017</div>
    <h3>Easy Managed<br>Time Can Save you Money</h3>
    <p>Lorem ipsum dolor sit amet, consectetuer adipiscing elit. Aenean commodo ligula eget dolor. Aenean massa. Cum sociis natoque penatibus et magnis dis parturient montes.</p>
    <div class="more">Read More</div>
  </article>
</section>

<section class="partners">
  <h2 class="section-title" style="top:44px;font-size:26px">Our Partners</h2>
  <div class="partner" style="left:162px"><span></span></div>
  <div class="partner" style="left:379px"><span></span></div>
  <div class="partner" style="left:594px"><span></span></div>
  <div class="partner" style="left:810px"><span></span></div>
  <div class="dots"><i></i><i></i><i></i><i></i></div>
</section>

<footer class="site-footer gradient">
  <div class="foot-mark"></div>
  <div class="contact">
    <div><svg width="10" height="10" viewBox="0 0 10 10"><path d="M2 0L4 2.5L3 4C4 6 5 7 6 7L7.5 6L10 8L8.5 10C4 10 0 6 0 1.5Z" fill="#fff"/></svg>+370 600 123 45</div>
    <div><svg width="11" height="8" viewBox="0 0 11 8"><rect width="11" height="8" rx="1" fill="#fff"/><path d="M0.5 0.8L5.5 4.5L10.5 0.8" stroke="#3a4be0" fill="none"/></svg>info@kestrelax.com</div>
    <div style="padding-left:18px">Company Name</div>
  </div>
  <div class="foot-col" style="left:417px">
    <h4>About kestrel AX</h4>
    <ul><li>Newsletter</li><li>Our Memberships</li><li>Events</li><li>Investors</li><li>Suppliers Response</li></ul>
  </div>
  <div class="foot-col" style="left:648px">
    <h4>Account</h4>
    <ul><li>Manage Your ID</li><li>kestrel AX Store</li><li>Customer Reviews</li><li>Ask a Question</li><li>Why choose us?</li></ul>
  </div>
  <div class="foot-col" style="left:869px">
    <h4>Apie Mus</h4>
    <ul><li>Inclusion and Diversity</li><li>Supplier Responsibility</li><li>Inclusion and Diversity</li><li>Shop for Business</li><li>Shop for Consumers</li></ul>
  </div>
  <div class="foot-rule"></div>
  <div class="copyright">Copyright 2018 kestrel AX | All rights reserved</div>
  <div class="socials"><i></i><i></i><i></i></div>
</footer>

</body>
</html>
```